Templates for Construction Company

We are looking to have templates prepared for all aspects of our letter sending. Using our brand design. with similar layouts that look the same.

Letterheads design & Email signatures

We use letter heads for - quotes, contract correspondence, variations, formal letters, invitations

Target Market(s)

Clients documents sent in emails

Industry/Entity Type

Construction

Font styles to use
Serif
Sans Serif

Colors
0054AA
0677BA
7BADD7
CADEEF
E8F1F8

Requirements
Must have
• Easy to read, water marks on page
Nice to have
• Different options for different letters

```html
<!DOCTYPE html>
<html lang="en">
<head>
<meta charset="utf-8">
<title>Kerbstone Building Group – Stationery</title>
<link href="https://fonts.googleapis.com/css2?family=Lato:wght@400;700&family=Roboto:wght@400;500&family=Pinyon+Script&display=swap" rel="stylesheet">
<style>
  :root {
    --backdrop: #e6e6e6;
    --paper: #f4f4f4;
    --brand-blue: #5082bf;
    --text-dark: #1e1e1e;
    --text-grey: #6a6a6a;
    --watermark: #e7e7e7;
  }
  * { box-sizing: border-box; margin: 0; padding: 0; }
  html, body { width: 1200px; height: 942px; overflow: hidden; }
  body { background: var(--backdrop); position: relative; font-family: "Roboto", sans-serif; }

  .sheet { position: absolute; background: var(--paper); overflow: hidden; }

  /* Letterhead */
  .letterhead { left: 157px; top: 151px; width: 436px; height: 616px; }
  .brand-name {
    position: absolute; font-family: "Roboto", sans-serif; font-weight: 500;
    color: var(--brand-blue); letter-spacing: -0.3px; line-height: 1;
  }
  .letterhead .brand-name { left: 37px; top: 34px; font-size: 28px; }
  .letterhead .watermark {
    position: absolute; left: 150px; top: 310px; font-size: 64px;
    font-weight: 500; color: var(--watermark); line-height: 1;
  }
  .sender-block {
    position: absolute; right: 37px; top: 25px; text-align: right;
    font-size: 7.4px; line-height: 8.8px; color: var(--text-grey);
  }
  .sender-block .contact { margin-top: 3px; }
  .contact-line { display: flex; justify-content: flex-end; align-items: center; gap: 4px; }
  .contact-line svg { width: 6px; height: 6px; fill: var(--brand-blue); }

  .letter-body {
    position: absolute; left: 46px; top: 205px; width: 343px;
    font-family: "Lato", sans-serif; font-size: 7.1px; line-height: 8.8px;
    color: var(--text-dark); text-align: justify;
  }
  .letter-body .salutation { font-weight: 700; margin-bottom: 8.8px; }
  .letter-body p { margin-bottom: 8.8px; }
  .sign-off { position: absolute; left: 46px; top: 416px; font-family: "Lato", sans-serif; font-size: 7.3px; color: var(--text-dark); }
  .signature { position: absolute; left: 45px; top: 436px; font-family: "Pinyon Script", cursive; font-size: 15px; color: var(--text-dark); }
  .signer-role { position: absolute; left: 46px; top: 455px; font-family: "Lato", sans-serif; font-size: 7.3px; color: var(--text-dark); }

  .web-band {
    position: absolute; left: 0; right: 0; background: var(--brand-blue);
    color: #fff; font-size: 7.2px; display: flex; align-items: center;
  }
  .letterhead .web-band { top: 595px; height: 14px; justify-content: center; letter-spacing: 0.8px; }

  /* Envelope front */
  .envelope-front { left: 624px; top: 298px; width: 501px; height: 216px; }
  .envelope-front .brand-name { left: 36px; top: 42px; font-size: 28px; }
  .envelope-front .watermark {
    position: absolute; right: 12px; top: 140px; font-size: 40px;
    font-weight: 500; color: var(--watermark); line-height: 1;
  }
  .return-address {
    position: absolute; left: 36px; top: 88px; font-size: 7.4px;
    line-height: 8.8px; color: var(--text-grey);
  }
  .envelope-front .web-band { top: 194px; height: 14px; padding-left: 36px; }

  /* Envelope back */
  .envelope-back { left: 624px; top: 550px; width: 501px; height: 217px; }
  .envelope-back svg.flap { position: absolute; left: 0; top: 0; }
  .envelope-back .brand-name {
    left: 0; right: 0; top: 29px; text-align: center; font-size: 17px; color: #fff;
  }
</style>
</head>
<body>

  <section class="sheet letterhead" aria-label="Letterhead">
    <div class="watermark" aria-hidden="true">Kerbstone</div>
    <div class="brand-name">Kerbstone</div>
    <address class="sender-block" style="font-style:normal">
      <div>Kerbstone Building Group Limited</div>
      <div>48 Harbour Lane, Kelburn</div>
      <div>Wellington 6012, New Zealand</div>
      <div class="contact">
        <div class="contact-line">+64 04 555 0182
          <svg viewBox="0 0 24 24" aria-hidden="true"><path d="M6.6 10.8a15.1 15.1 0 0 0 6.6 6.6l2.2-2.2a1 1 0 0 1 1-.25 11.4 11.4 0 0 0 3.6.57 1 1 0 0 1 1 1V20a1 1 0 0 1-1 1A17 17 0 0 1 3 4a1 1 0 0 1 1-1h3.5a1 1 0 0 1 1 1c0 1.25.2 2.45.57 3.57a1 1 0 0 1-.25 1z"/></svg>
        </div>
        <div class="contact-line">info@kerbstonebuilding.co.nz
          <svg viewBox="0 0 24 24" aria-hidden="true"><path d="M2 5h20v14H2zm2 2v.5l8 5 8-5V7l-8 5z"/></svg>
        </div>
      </div>
    </address>

    <div class="letter-body">
      <div class="salutation">Dear Daniel Hartley,</div>
      <p>Lorem ipsum dolor sit amet, consectetuer adipiscing elit, sed diam nonummy nibh euismod tincidunt ut laoreet dolore magna aliquam erat volutpat. Ut wisi enim ad minim veniam, quis nostrud exerci tation ullamcorper suscipit lobortis nisl ut aliquip ex ea commodo consequat. Duis dolore te feugait nulla facilisi. Nam liber tempor cum soluta nobis eleifend option congue nihil imperdiet doming id quod mazim placerat facer possim assum. Lorem ipsum dolor sit amet, consectetuer adipiscing elit, sed diam nonummy nibh euismod tincidunt ut laoreet dolore magna aliquam erat volutpat. Ut wisi enim ad minim veniam, quis nostrud exerci tation ullamcorper suscipit lobortis nisl ut aliquip ex ea commodo consequat.</p>
      <p>Consectetuer adipiscing elit, sed diam nonummy nibh euismod tincidunt ut laoreet dolore magna aliquam erat volutpat. Ut wisi enim ad minim veniam, quis nostrud exerci tation ullamcorper suscipit lobortis nisl ut aliquip ex ea commodo consequat. Consectetuer adipiscing elit, sed diam nonummy nibh euismod tincidunt ut laoreet dolore magna aliquam erat volutpat. Ut wisi enim ad minim veniam, quis nostrud exerci tation ullamcorper suscipit lobortis nisl ut aliquip ex ea commodo consequat.</p>
      <p>Consectetuer adipiscing elit, sed diam nonummy nibh euismod tincidunt ut laoreet dolore magna aliquam erat volutpat. Ut wisi enim ad minim veniam, quis nostrud exerci tation ullamcorper suscipit lobortis nisl ut aliquip ex ea commodo consequat. Consectetuer adipiscing elit, sed diam nonummy nibh euismod tincidunt ut laoreet dolore magna aliquam erat volutpat. Ut wisi enim ad minim veniam, quis nostrud exerci tation ullamcorper suscipit lobortis nisl ut aliquip ex ea commodo consequat.</p>
    </div>
    <div class="sign-off">Sincerely Yours</div>
    <div class="signature">Thomas Avery</div>
    <div class="signer-role">General Manager</div>

    <div class="web-band">www.kerbstonebuilding.co.nz</div>
  </section>

  <section class="sheet envelope-front" aria-label="Envelope front">
    <div class="watermark" aria-hidden="true">Kerbstone</div>
    <div class="brand-name">Kerbstone</div>
    <address class="return-address" style="font-style:normal">
      <div>Kerbstone Building Group Limited</div>
      <div>48 Harbour Lane, Kelburn</div>
      <div>Wellington 6012, New Zealand</div>
    </address>
    <div class="web-band">www.kerbstonebuilding.co.nz</div>
  </section>

  <section class="sheet envelope-back" aria-label="Envelope back">
    <svg class="flap" width="501" height="217" viewBox="0 0 501 217" aria-hidden="true">
      <path d="M15 52 Q6 55 6 66 L3 217 M486 52 Q495 55 495 66 L498 217" fill="none" stroke="#cfcfcf" stroke-width="0.8"/>
      <defs>
        <linearGradient id="flapFill" x1="0" x2="1">
          <stop offset="0" stop-color="#4a78b6"/>
          <stop offset="1" stop-color="#5a8cc7"/>
        </linearGradient>
      </defs>
      <path d="M0 0 H501 L484 62 Q481 71 470 71 H31 Q20 71 17 62 Z" fill="url(#flapFill)"/>
    </svg>
    <div class="brand-name">Kerbstone</div>
  </section>

</body>
</html>
```